Chiropody and Podiatry Flyer

A6 Flyer for a Chiropody Clinic.
Need to use an existing company logo (upload available).
Flyer should promote three aspects of the practice;
1) General chiropody : Nail Cutting; Corn Removal; Ingrown Nails; Hard Skin Removal; Verruca Treatment; Diabetic Assessment; Nail Surgery.
2) Home Visits - chiropody in the comfort of your own home.
3) Biomechanical Assessments / Orthotics
Colours should comprise navy blue/green/white to complement existing logo.
Promotional Offer on flyer.

Industry/Entity Type

Clinic

```html
<!DOCTYPE html>
<html lang="en">
<head>
<meta charset="utf-8">
<title>Ember Vale Foot Clinic – Flyer</title>
<link href="https://fonts.googleapis.com/css2?family=Great+Vibes&family=Montserrat:wght@600;700&family=Questrial&display=swap" rel="stylesheet">
<style>
  :root {
    --backdrop: #ecebe8;
    --paper: #ffffff;
    --charcoal: #353535;
    --green: #3fd43a;
    --navy: #0f2a63;
    --navy-deep: #081a40;
    --white: #ffffff;
    --badge-grey: #b9bcc4;
    --plate-grey: #e4e5e8;
  }
  * { margin: 0; padding: 0; box-sizing: border-box; }
  html, body { width: 1200px; height: 594px; overflow: hidden; background: var(--backdrop); }
  .flyer {
    position: absolute; left: 108px; top: 87px; width: 983px; height: 420px;
    background: var(--paper);
    box-shadow: 0 2px 10px rgba(0,0,0,0.12);
  }

  .hero {
    position: absolute; left: 33px; top: 33px; width: 459px; height: 353px;
    background:
      radial-gradient(ellipse 55% 50% at 76% 28%, #fff8dc 0%, #f5dc96 40%, rgba(240,190,90,0) 78%),
      radial-gradient(ellipse 65% 75% at 32% 55%, #c9782e 0%, #e2a552 48%, rgba(226,165,82,0) 82%),
      linear-gradient(165deg, #f4e7c4 0%, #e8bd6c 45%, #c98a45 75%, #ece2d4 100%);
    overflow: hidden;
  }
  .tagline {
    position: absolute; inset: 0; color: var(--white);
    font-family: 'Great Vibes', cursive; font-size: 44px; line-height: 1;
    text-shadow: 0 1px 4px rgba(120,60,10,0.25);
  }
  .tagline span { position: absolute; white-space: nowrap; }
  .tagline .t1 { left: 262px; top: 126px; }
  .tagline .t2 { left: 288px; top: 170px; }
  .tagline .t3 { left: 306px; top: 212px; }

  .offer {
    position: absolute; left: 0; bottom: 0; width: 100%; height: 46px;
    background: var(--navy);
    border-top: 3px solid var(--green);
    display: flex; align-items: center; justify-content: center; gap: 10px;
    font-family: 'Montserrat', sans-serif; font-weight: 700; font-size: 12.5px;
    letter-spacing: 0.4px;
  }
  .offer .label { color: var(--green); }
  .offer .deal { color: var(--white); }

  .services {
    position: absolute; left: 492px; top: 33px; width: 458px; height: 175px;
    background: var(--charcoal); text-align: center; padding-top: 42px;
  }
  .services .heading {
    font-family: 'Montserrat', sans-serif; font-weight: 700; font-size: 11.5px;
    color: var(--green); line-height: 21px; letter-spacing: 0.2px;
  }
  .services .detail {
    font-family: 'Questrial', sans-serif; font-size: 12.5px;
    color: var(--white); line-height: 21px;
  }

  .credentials {
    position: absolute; left: 492px; top: 208px; width: 458px; height: 112px;
    background: var(--paper);
  }
  .badge-register {
    position: absolute; left: 45px; top: 84px; width: 78px; height: 16px;
    background: var(--navy); border: 1px solid var(--badge-grey);
  }
  .brand {
    position: absolute; left: 171px; top: 12px; width: 114px; height: 83px;
    background: linear-gradient(180deg, var(--navy-deep), var(--navy));
    display: flex; align-items: center; justify-content: center; flex-direction: column;
    gap: 6px;
  }
  .brand .mark { width: 14px; height: 14px; border-radius: 50%; background: var(--green); }
  .brand .name {
    font-family: 'Questrial', sans-serif; font-size: 11px; color: var(--white);
    text-align: center; line-height: 13px; letter-spacing: 0.5px;
  }
  .badge-society {
    position: absolute; left: 335px; top: 72px; width: 20px; height: 22px;
    background: var(--badge-grey); border-radius: 3px 3px 10px 10px;
  }
  .badge-society-plate {
    position: absolute; left: 360px; top: 74px; width: 60px; height: 18px;
    background: var(--plate-grey);
  }

  .contact {
    position: absolute; left: 492px; top: 320px; width: 458px; height: 66px;
    background: var(--charcoal); color: var(--white);
    font-family: 'Montserrat', sans-serif; font-weight: 600; font-size: 12.3px;
    line-height: 17px; padding: 9px 0 0 44px;
  }
  .contact .phone { display: inline-flex; align-items: center; gap: 4px; margin-left: 6px; }
  .contact svg { width: 12px; height: 12px; }
</style>
</head>
<body>
  <div class="flyer">
    <div class="hero" role="img" aria-label="Photograph of a woman with red hair, eyes closed, face lifted towards warm golden sunlight, with a faint phoenix ornament on the right">
      <div class="tagline">
        <span class="t1">Restore</span>
        <span class="t2">Renew</span>
        <span class="t3">Revitalise</span>
      </div>
      <div class="offer">
        <span class="label">NEW PATIENT OFFER</span>
        <span class="deal">20% OFF YOUR FIRST TREATMENT</span>
      </div>
    </div>

    <section class="services">
      <p class="heading">1) GENERAL CHIROPODY :</p>
      <p class="detail">Nail Cutting | Corn Removal | Ingrown Nails | Hard Skin Removal</p>
      <p class="detail">Verruca Treatment | Diabetic Assessment | Nail Surgery.</p>
      <p class="heading">2) HOME VISITS</p>
      <p class="detail">Chiropody in the comfort of your own home.</p>
      <p class="heading">3) BIOMECHANICAL ASSESSMENTS / ORTHOTICS</p>
    </section>

    <section class="credentials">
      <div class="badge-register" role="img" aria-label="Professional registration badge"></div>
      <div class="brand">
        <div class="mark"></div>
        <p class="name">EMBER VALE<br>FOOT CLINIC</p>
      </div>
      <div class="badge-society" role="img" aria-label="Professional society membership badge"></div>
      <div class="badge-society-plate" role="img" aria-label="Professional society name plate"></div>
    </section>

    <footer class="contact">
      4B, Larkfield House, Millbrook Estate, Orchard Lane, Westmere,<br>
      Dunford Essex, DN7 2QT
      <span class="phone">
        <svg viewBox="0 0 12 12" aria-hidden="true"><circle cx="6" cy="6" r="6" fill="#3fd43a"/><path d="M3.6 3.2c.3-.3.7-.3.9 0l.7.9c.2.3.2.6-.1.8l-.4.3c.3.8 1 1.5 1.8 1.8l.3-.4c.2-.3.5-.3.8-.1l.9.7c.3.2.3.6 0 .9l-.5.5c-.5.5-2 .1-3.3-1.2S2.6 4.2 3.1 3.7z" fill="#353535"/></svg>
        07700 900418
      </span>
      <span class="phone">
        <svg viewBox="0 0 12 12" aria-hidden="true"><circle cx="6" cy="6" r="6" fill="#3fd43a"/><path d="M3.6 3.2c.3-.3.7-.3.9 0l.7.9c.2.3.2.6-.1.8l-.4.3c.3.8 1 1.5 1.8 1.8l.3-.4c.2-.3.5-.3.8-.1l.9.7c.3.2.3.6 0 .9l-.5.5c-.5.5-2 .1-3.3-1.2S2.6 4.2 3.1 3.7z" fill="#353535"/></svg>
        01632 960254
      </span>
    </footer>
  </div>
</body>
</html>
```